Real Estate Media Company Business Card

’m looking for a modern, high-end, double-sided business card for:
Brightpath Studio LLC
(Real Estate Photography & Videography)
The design should feel clean, minimal, and premium, appealing to top real estate agents and brokers.
👉 Horizontal layout is preferred
👉 Vertical option is welcome but not required
⸻
Front Side (Main Information):
Include:
* Tobias Wrenfield
* Brightpath Studio LLC
* Title (open to creative improvement)
* Phone Number
* Email
* Website
⸻
Services Section (VERY IMPORTANT):
This should be a key visual element, not an afterthought.
Services to Include:
* Cinematic Video
* Real Estate Photography
* Drone
* Social Media Reels
* Floor Plans
* Use clean, modern icons next to each service
* Icons should be simple, minimal, and consistent style (outline or thin line preferred)
* Option to place icons inside small circles (like reference)
Layout:
* Format services similar to a clean horizontal or grid-style list (like “example 2”)
* Keep spacing balanced and uncluttered
* Make this section visually appealing and easy to scan
⸻
Back Side:
* Keep it extremely minimal
* Only include the logo in a corner
* No additional text needed
⸻
Typography & Style:
* Modern, clean, slightly bold fonts (based on uploaded references)
* Strong hierarchy (name + services stand out most)
* Plenty of white/negative space
* Avoid clutter
⸻
Overall Feel:
* Luxury
* Modern
* Clean
* Confident
* High-end real estate branding
⸻
Notes for Designers:
* Simplicity is key
* Services section should feel polished and intentional
* This card should feel like something a top-producing real estate agent would keep
Real estate agent agents

```html
<!DOCTYPE html>
<html lang="en">
<head>
<meta charset="utf-8">
<title>Brightpath Studio – Business Card</title>
<link href="https://fonts.googleapis.com/css2?family=Ubuntu:wght@300;400;500;700&display=swap" rel="stylesheet">
<style>
  :root{
    --bg:#e6e7e9;
    --ink:#000000;
    --paper:#ffffff;
    --gold:#c9a131;
    --rule:#8a8a8a;
    --dark-text:#141414;
  }
  *{box-sizing:border-box;margin:0;padding:0}
  html,body{width:1200px;height:1200px;overflow:hidden;background:var(--bg)}
  body{position:relative;font-family:"Ubuntu",sans-serif}

  .card{position:absolute;left:130px;width:940px;height:522px;overflow:hidden;border-radius:43px}
  .card--front{top:50px;background:var(--ink);color:var(--paper)}
  .card--back{top:628px;background:var(--paper)}
  .card__scale{position:absolute;left:0;top:0;width:870px;height:483px;transform:scale(1.0805);transform-origin:0 0}
  .card__notch{position:absolute;left:0;top:0;width:870px;height:483px}

  .accent-bar{position:absolute;height:4px;width:52px;background:var(--gold)}
  .accent-bar--top{left:52px;top:42px}
  .accent-bar--mid{left:52px;top:269px;height:3px}

  .brand-name{position:absolute;left:52px;top:84px;font-size:26px;font-weight:400;letter-spacing:2.5px;color:var(--paper);text-transform:uppercase}

  .person{position:absolute;left:52px;top:168px}
  .person__name{font-size:44px;font-weight:700;line-height:1.1}
  .person__title{font-size:24px;font-weight:300;color:var(--gold);margin-top:2px}

  .contact{position:absolute;left:52px;top:300px;list-style:none}
  .contact__item{display:flex;align-items:center;height:51px;font-size:22px;font-weight:300}
  .contact__icon{width:36px;height:36px;margin-right:23px;flex:none}

  .divider{position:absolute;left:497px;top:77px;width:3px;height:329px;background:var(--gold)}

  .services{position:absolute;left:535px;top:98px;width:335px}
  .services__heading{font-size:26px;font-weight:700;letter-spacing:4.5px}
  .services__list{list-style:none;margin-top:18px}
  .service{position:relative;display:flex;align-items:center;height:50px;border-bottom:1px solid var(--rule);margin-left:50px;padding-left:36px}
  .service:last-child{border-bottom:none}
  .service__icon{position:absolute;left:-54px;top:7px;width:46px;height:36px}
  .service__tick{position:absolute;left:15px;top:9px;width:3px;height:32px;background:var(--gold)}
  .service__label{font-size:15px;font-weight:500;text-transform:uppercase;letter-spacing:.2px;white-space:nowrap}

  .back-mark{position:absolute;right:62px;top:120px;display:flex;align-items:center;gap:14px}
  .back-mark__dot{width:18px;height:18px;border:2px solid var(--dark-text);border-radius:50%}
  .back-mark__name{font-size:32px;font-weight:400;letter-spacing:3px;color:var(--dark-text);text-transform:uppercase}
</style>
</head>
<body>

<section class="card card--front" aria-label="Front of business card">
  <div class="card__scale">
    <span class="accent-bar accent-bar--top"></span>
    <div class="brand-name">Brightpath Studio LLC</div>

    <div class="person">
      <h1 class="person__name">Tobias Wrenfield</h1>
      <p class="person__title">Founder &amp; Real Estate Media Specialist</p>
    </div>
    <span class="accent-bar accent-bar--mid"></span>

    <ul class="contact">
      <li class="contact__item">
        <svg class="contact__icon" viewBox="0 0 36 36" fill="none" stroke="#fff" stroke-width="2.4"><rect x="10" y="2" width="16" height="32" rx="3"/><line x1="10" y1="7" x2="26" y2="7"/><line x1="10" y1="29" x2="26" y2="29"/></svg>
        (555) 014 2288
      </li>
      <li class="contact__item">
        <svg class="contact__icon" viewBox="0 0 36 36" fill="none" stroke="#fff" stroke-width="2.4"><rect x="2" y="8" width="32" height="21"/><polyline points="2,8 18,21 34,8"/><line x1="2" y1="29" x2="14" y2="18"/><line x1="34" y1="29" x2="22" y2="18"/></svg>
        tobias@brightpathstudio.com
      </li>
      <li class="contact__item">
        <svg class="contact__icon" viewBox="0 0 36 36" fill="none" stroke="#fff" stroke-width="2"><circle cx="18" cy="18" r="15"/><ellipse cx="18" cy="18" rx="7" ry="15"/><line x1="3" y1="18" x2="33" y2="18"/><path d="M6 10h24M6 26h24"/></svg>
        brightpathstudio.com
      </li>
    </ul>

    <span class="divider"></span>

    <div class="services">
      <h2 class="services__heading">SERVICES</h2>
      <ul class="services__list">
        <li class="service">
          <svg class="service__icon" viewBox="0 0 46 36" fill="none" stroke="#fff" stroke-width="2"><rect x="4" y="8" width="38" height="24" rx="2"/><path d="M15 8l3-5h10l3 5"/><circle cx="23" cy="20" r="8"/><circle cx="23" cy="20" r="5"/><line x1="4" y1="13" x2="15" y2="13"/></svg>
          <span class="service__tick"></span><span class="service__label">Real Estate Photography</span>
        </li>
        <li class="service">
          <svg class="service__icon" viewBox="0 0 46 36" fill="none" stroke="#fff" stroke-width="2"><circle cx="12" cy="8" r="6"/><circle cx="24" cy="8" r="6"/><rect x="5" y="15" width="27" height="18" rx="2"/><rect x="9" y="22" width="12" height="7"/><polygon points="32,21 42,15 42,33 32,27"/></svg>
          <span class="service__tick"></span><span class="service__label">Cinematic Video</span>
        </li>
        <li class="service">
          <svg class="service__icon" viewBox="0 0 46 36" fill="none" stroke="#fff" stroke-width="2"><line x1="2" y1="8" x2="16" y2="8"/><line x1="30" y1="8" x2="44" y2="8"/><line x1="9" y1="5" x2="9" y2="13"/><line x1="37" y1="5" x2="37" y2="13"/><path d="M9 13l8 4h12l8-4"/><rect x="16" y="15" width="14" height="8" rx="3" fill="#fff"/><path d="M17 23l-5 8M29 23l5 8"/><circle cx="23" cy="27" r="3"/></svg>
          <span class="service__tick"></span><span class="service__label">Scope Drone / Aerial</span>
        </li>
        <li class="service">
          <svg class="service__icon" viewBox="0 0 46 36" fill="none" stroke="#fff" stroke-width="2"><rect x="10" y="3" width="30" height="31"/><path d="M10 3c-4 0-6 2-6 5v26h6"/><rect x="15" y="9" width="20" height="19"/><line x1="25" y1="9" x2="25" y2="15"/><line x1="25" y1="20" x2="25" y2="28"/><line x1="15" y1="18" x2="20" y2="18"/></svg>
          <span class="service__tick"></span><span class="service__label">Floor Plan</span>
        </li>
        <li class="service">
          <svg class="service__icon" viewBox="0 0 46 36" fill="none" stroke="#fff" stroke-width="2"><rect x="13" y="1" width="20" height="34" rx="3"/><line x1="13" y1="6" x2="33" y2="6"/><line x1="13" y1="30" x2="33" y2="30"/><polygon points="20,12 28,18 20,24" fill="#fff"/></svg>
          <span class="service__tick"></span><span class="service__label">Social Media Reels</span>
        </li>
      </ul>
    </div>

    <svg class="card__notch" viewBox="0 0 870 483" aria-hidden="true">
      <rect x="523" y="412" width="200" height="140" rx="25" fill="var(--bg)"/>
      <path d="M718 450 L778 413 Q787 408 787 418 L787 560 L718 560 Z" fill="var(--bg)"/>
    </svg>
  </div>
</section>

<section class="card card--back" aria-label="Back of business card">
  <div class="card__scale">
    <div class="back-mark">
      <span class="back-mark__dot"></span>
      <span class="back-mark__name">Brightpath Studio</span>
    </div>
    <svg class="card__notch" viewBox="0 0 870 483" aria-hidden="true">
      <rect x="147" y="412" width="200" height="140" rx="25" fill="var(--bg)"/>
      <path d="M152 450 L92 413 Q83 408 83 418 L83 560 L152 560 Z" fill="var(--bg)"/>
    </svg>
  </div>
</section>

</body>
</html>
```